Travel Blogger Business Card for roamquill.net

I need a two-sided business card for a travel blogging website. The card should be both professional and fun at the same time. This is for the website www.roamquill.net

I don't necessarily think that the current logo on the website needs to be used on the business card but it can be. I am very flexible with ideas

Target Market(s)

Travel agencies that will be met at a conference.

Industry/Entity Type

Travel

Contact Information for Business Card

Company Name: Roam Quill.net
Name: Bertrand Olesky
Voice: +1-(555)-402-7731
Address: Coral Reach Shore, Port Halden, Saltmere Isles
Email: ceo@roamquill.net

Colors
0592cd
0355a3
3176b5
33a6d7
85cae6
85acd3

Requirements
Must have
• Website address and name should be bigger than address, phone number, and email.

```html
<!DOCTYPE html>
<html lang="en">
<head>
<meta charset="utf-8">
<title>Roam Quill.net — Business Card</title>
<link href="https://fonts.googleapis.com/css2?family=Archivo:wdth,wght@125,800&family=PT+Sans:wght@400&display=swap" rel="stylesheet">
<style>
  :root {
    --ink: #000000;
    --frame-blue: #0355a3;
    --panel-blue: #85acd3;
    --paper: #ffffff;
    --display: "Archivo", sans-serif;
    --body: "PT Sans", sans-serif;
  }
  * { margin: 0; padding: 0; box-sizing: border-box; }
  html, body {
    width: 1200px; height: 1000px; overflow: hidden;
    background: var(--paper);
  }
  .canvas { position: relative; width: 1200px; height: 1000px; }

  .card {
    position: absolute; top: 343px; width: 548px; height: 313px;
    background: var(--frame-blue);
  }
  .card--front { left: 20px; }
  .card--back { left: 633px; width: 547px; }

  .card__panel {
    position: absolute; left: 17px; top: 18px; width: 514px; height: 276px;
    background: var(--panel-blue); border-radius: 12px; overflow: hidden;
  }
  .card--back .card__panel { width: 513px; }

  .brand { position: absolute; left: 16px; display: flex; align-items: center; gap: 12px; }
  .brand__dot {
    width: 36px; height: 36px; border-radius: 50%; background: var(--ink); flex: none;
  }
  .brand__name {
    font-family: var(--display); font-weight: 800; font-stretch: 125%;
    font-size: 38px; line-height: 38px; color: var(--ink);
    white-space: nowrap; letter-spacing: -0.5px;
  }
  .card--front .brand { top: 42px; }
  .card--back .brand { top: 125px; }

  .holder {
    position: absolute; right: 16px; top: 120px;
    font-family: var(--display); font-weight: 800; font-stretch: 125%;
    font-size: 21px; line-height: 24px; color: var(--ink); white-space: nowrap;
  }
  .divider {
    position: absolute; left: 16px; right: 16px; top: 150px;
    height: 1.5px; background: var(--ink);
  }
  .address {
    position: absolute; left: 16px; top: 158px;
    font-family: var(--body); font-size: 15px; line-height: 20px; color: var(--ink);
  }
  .contacts {
    position: absolute; left: 320px; top: 157px; list-style: none;
    font-family: var(--body); font-size: 15px; color: var(--ink);
  }
  .contacts li { display: flex; align-items: center; gap: 10px; height: 27px; margin-bottom: 6px; white-space: nowrap; }
  .contacts svg { width: 27px; height: 27px; flex: none; }

  .website {
    position: absolute; left: 0; right: 0; text-align: center;
    font-family: var(--body); font-size: 22px; line-height: 28px; letter-spacing: 4px;
  }
  .card--front .website { top: 244px; color: var(--ink); }

  .band {
    position: absolute; left: 0; right: 0; top: 172px; height: 38px;
    background: var(--frame-blue);
  }
  .band .website { top: 4px; color: var(--paper); letter-spacing: 7px; }
</style>
</head>
<body>
<main class="canvas">

  <section class="card card--front" aria-label="Card front">
    <div class="card__panel">
      <div class="brand">
        <span class="brand__dot"></span>
        <span class="brand__name">ROAM QUILL.NET</span>
      </div>
      <p class="holder">Bertrand Olesky</p>
      <div class="divider"></div>
      <p class="address">Coral Reach Shore, Port Halden<br>Saltmere Isles</p>
      <ul class="contacts">
        <li>
          <svg viewBox="0 0 28 28" aria-hidden="true">
            <circle cx="14" cy="14" r="14" fill="#0355a3"/>
            <path d="M10.2 7.5l2.4 2.9-1.5 1.7c.9 1.9 2.3 3.3 4.2 4.2l1.7-1.5 2.9 2.4-1.6 2.4c-5 -.6-9.5-5.1-10.1-10.1z" fill="#fff"/>
          </svg>
          +1-(555)-402-7731
        </li>
        <li>
          <svg viewBox="0 0 28 28" aria-hidden="true">
            <circle cx="14" cy="14" r="14" fill="#0355a3"/>
            <rect x="7" y="9" width="14" height="10" fill="#fff"/>
            <polyline points="7,9 14,15 21,9" fill="none" stroke="#0355a3" stroke-width="1.2"/>
            <line x1="7" y1="19" x2="12" y2="14" stroke="#0355a3" stroke-width="1"/>
            <line x1="21" y1="19" x2="16" y2="14" stroke="#0355a3" stroke-width="1"/>
          </svg>
          ceo@roamquill.net
        </li>
      </ul>
      <p class="website">www.roamquill.net</p>
    </div>
  </section>

  <section class="card card--back" aria-label="Card back">
    <div class="card__panel">
      <div class="brand">
        <span class="brand__dot"></span>
        <span class="brand__name">ROAM QUILL.NET</span>
      </div>
      <div class="band">
        <p class="website">www.roamquill.net</p>
      </div>
    </div>
  </section>

</main>
</body>
</html>
```